Larkmoor Web Design Project

I need the front page and an internal page designed for this client's website. The logo is attached. Obviously the colors have to go with and/or work with the logo colors. I also attached a very rough brochure layout to help you see the direction we're going in with print materials. The rough site map is also attached. I see a slider on the homepage, the art for which I may come back to you to create. This clinic is in a very high end Dallas neighborhood. The hook is that it's a primary care and urgent facility with convenient hours.

I don't know how much this impacts your design, but this will be a Wordpress site and I'm using a framework called PageLines (framevault.example). If PageLines proves to be inflexible, I'll have to get a template that allows me to execute your design.

This site (http://sundaleclinicgroup.example) has the type and quality of content I will eventually have on the Larkmoor site.
Updates

I just revised the brief for this project. I added the site map and added details to the overview and the "Must Have" section. Thank you for revisiting the brief. 

Reason: Christmas was a bad time to end it.

Target Market(s)

Women 25-54 with children living at home, income over $150k/year

Industry/Entity Type

Clinic

Requirements
Must have
• Masthead incorporating the logo
Followed by the primary nav
Slider on the home page below that
Dual nav - 1 with the nav in the attached site map
2 secondary nav with areas of healthcare
There will three blocks under the nav
1. It's about time (with a small blurb less than 50 words.
2. It's about choices (with small blurb)
3. It's about you (with small blurb)
Three footer blocks
patient check in link on every page
"No appointment? No problem" icon on every page

```html
<!DOCTYPE html>
<html lang="en">
<head>
<meta charset="utf-8">
<title>Larkmoor Medical</title>
<link rel="stylesheet" href="https://fonts.googleapis.com/css2?family=Questrial&family=Arimo:wght@400;700&family=Noto+Serif:ital,wght@1,400;1,700&display=swap">
<style>
:root{
  --blue:#1f66ae;
  --blue-dark:#1a5596;
  --blue-footer:#3d6fae;
  --green:#2f9a3e;
  --green-dark:#1f7f2e;
  --orange:#f08a1c;
  --red:#d44b32;
  --paper:#ece8e2;
  --card:#fbfaf8;
  --ink:#333;
  --muted:#666;
  --line:#d8d3cb;
  --footer-mark:#a9bfd9;
}
*{box-sizing:border-box;margin:0;padding:0}
html,body{width:811px;height:1200px;overflow:hidden}
body{position:relative;background:var(--paper);font-family:"Arimo",Arial,sans-serif;color:var(--ink);font-size:9px}
.abs{position:absolute}
ul{list-style:none}

/* masthead */
.masthead{left:0;top:0;width:811px;height:79px;background:#fff}
.masthead::after{content:"";position:absolute;left:0;top:79px;width:811px;height:4px;background:var(--blue)}
.brand{left:96px;top:28px;display:flex;align-items:center;gap:7px}
.brand-dot{width:28px;height:28px;border-radius:50%;background:var(--blue)}
.brand-name{font-family:"Questrial",sans-serif;font-size:21px;color:var(--blue)}
.account{top:15px;height:16px;border-radius:2px;color:#fff;font-size:8.5px;display:flex;align-items:center;justify-content:center;gap:4px}
.account.register{left:513px;width:63px;background:var(--blue)}
.account.login{left:583px;width:62px;background:var(--green)}
.account.blog{left:653px;width:63px;background:var(--orange)}
.primary-nav{left:336px;top:38px;height:28px;display:flex;font-family:"Questrial",sans-serif;font-size:11px;color:#333}
.primary-nav li{padding:0 10px;line-height:28px}
.primary-nav li.active{background:var(--green);color:#fff;padding:0 10px}
.services-menu{left:434px;top:64px;width:126px;background:#fff;border-top:4px solid var(--green);box-shadow:0 2px 4px rgba(0,0,0,.25);z-index:5;padding:2px 0}
.services-menu li{height:19px;line-height:19px;padding-left:29px;position:relative;font-size:8.5px;color:#444;border-bottom:1px solid #eee}
.services-menu li:last-child{border-bottom:0}
.services-menu li::before{content:"";position:absolute;left:15px;top:6px;width:6px;height:6px;border-radius:50%;background:var(--blue)}

/* hero */
.hero{left:0;top:83px;width:811px;height:285px;background:linear-gradient(180deg,#3e8fd6 0%,#86bde8 45%,#b9d8ec 62%,#6fae45 82%,#4f962c 100%)}
.hero-title{left:96px;top:114px;font-family:"Questrial",sans-serif;font-weight:400;font-size:24px;line-height:29px;color:#fff}
.appointment{left:96px;top:197px;width:292px;height:125px;background:#fff;border-left:4px solid var(--green);box-shadow:0 2px 6px rgba(0,0,0,.3);padding:11px 12px}
.appointment h2{font-family:"Questrial",sans-serif;font-weight:400;font-size:14px;color:var(--blue);border-bottom:1px solid #e3e3e3;padding-bottom:5px}
.field{position:absolute;width:124px;height:20px;border:1px solid #ccc;font-size:8.5px;color:#777;line-height:18px;padding-left:18px}
.field::before{content:"";position:absolute;left:5px;top:6px;width:7px;height:6px;background:#999;border-radius:1px}
.hint{left:384px;top:239px;background:#222;color:#fff;font-size:7.5px;padding:3px 6px}
.required{position:absolute;left:10px;top:99px;color:#d22;font-size:7.5px}
.submit{position:absolute;left:228px;top:93px;width:53px;height:18px;background:var(--green);color:#fff;font-weight:700;font-size:9.5px;text-align:center;line-height:18px;border-radius:2px}
.slide-arrow{top:219px;width:30px;height:30px;border-radius:50%;background:rgba(90,90,90,.75);border:2px solid #fff}
.slide-arrow.prev{left:13px}.slide-arrow.next{left:769px}

/* welcome */
.welcome{left:0;top:388px;width:811px;text-align:center;font-family:"Questrial",sans-serif;font-weight:400;font-size:17px;color:var(--blue)}
.welcome span{color:var(--green)}
.welcome-rule{left:97px;top:417px;width:619px;height:1px;background:var(--line)}
.welcome-dot{left:399px;top:411px;width:13px;height:13px;border-radius:50%;background:var(--blue)}
.feature{top:455px;width:182px;height:131px;background:var(--card);border:1px solid #ddd;box-shadow:0 1px 3px rgba(0,0,0,.15);text-align:center;padding:30px 14px 0}
.feature h3{font-family:"Questrial",sans-serif;font-weight:400;font-size:10px;color:var(--green);margin-bottom:3px}
.feature p{font-size:7.5px;line-height:11.5px;color:#444}
.feature-icon{position:absolute;left:73px;top:-18px;width:36px;height:36px;border-radius:50%;background:var(--blue);border:3px solid #fff;box-shadow:0 0 0 1px #ccc}

/* lab */
.lab{left:96px;top:626px;width:399px;height:365px;background:var(--card);box-shadow:0 1px 4px rgba(0,0,0,.2)}
.lab h2{position:absolute;left:13px;top:19px;font-family:"Questrial",sans-serif;font-weight:400;font-size:12px;color:var(--blue)}
.lab-intro{position:absolute;left:13px;top:37px;width:372px;font-size:8.5px;line-height:11px;color:#444}
.lab-photo{position:absolute;left:14px;top:70px;width:111px;height:146px;background:linear-gradient(160deg,#a4b9c9,#d9c3a3 55%,#8aa865);border:2px solid #fff;box-shadow:0 0 2px rgba(0,0,0,.4)}
.lab-text{position:absolute;left:138px;top:70px;width:248px;font-size:8.5px;line-height:12px;color:#444}
.tests{position:absolute;left:138px;top:122px}
.tests li{font-family:"Noto Serif",serif;font-style:italic;font-size:9.5px;color:#222;height:18px;padding-left:13px;position:relative}
.tests li::before{content:"☆";position:absolute;left:0;top:0;font-style:normal;color:var(--blue);font-size:9px}
.read-more{position:absolute;left:138px;top:202px;width:50px;height:14px;background:var(--red);color:#fff;font-size:8px;text-align:center;line-height:14px;border-radius:2px}
.quote{position:absolute;left:12px;top:245px;width:373px;height:59px;background:#fff;border:1px solid #ddd;padding:9px 11px;font-style:italic;font-size:8px;line-height:12px;color:#666}
.avatar{position:absolute;left:16px;top:310px;width:40px;height:40px;border-radius:50%;background:#7a8d9c;border:3px solid #fff;box-shadow:0 0 2px rgba(0,0,0,.4)}
.person{position:absolute;left:65px;top:312px;font-size:7.5px;line-height:10px;color:#555}
.person b{display:block;font-weight:400;font-size:9px;color:var(--blue);margin-bottom:2px}
.view-all{position:absolute;left:321px;top:325px;width:51px;height:16px;background:var(--red);color:#fff;font-size:8px;text-align:center;line-height:16px;border-radius:2px}

/* sidebar */
.no-appt{left:535px;top:626px;width:181px;height:38px;background:linear-gradient(#5b8fc8,#3f73b3);color:#fff;font-size:9.5px;line-height:11px;padding:8px 0 0 37px}
.search{left:535px;top:675px;width:181px;height:29px;background:#fff;border:1px solid #ddd;padding:5px 7px}
.search div{height:18px;border:1px solid #ccc;font-size:8.5px;line-height:16px;padding-left:5px;color:#555;position:relative}
.video{left:538px;top:717px;width:176px;height:97px;background:linear-gradient(135deg,#b89a82,#d9c1a9 50%,#8a9aa7);border:3px solid #fff;box-shadow:0 0 2px rgba(0,0,0,.35)}
.play{position:absolute;left:74px;top:34px}
.subscribe{left:538px;top:830px;width:176px;height:139px;background:var(--green);border:3px solid #fff;box-shadow:0 0 2px rgba(0,0,0,.35)}
.subscribe h2{position:absolute;left:10px;top:7px;font-family:"Questrial",sans-serif;font-weight:400;font-size:21px;color:#fff}
.feed-dot{position:absolute;left:133px;top:6px;width:32px;height:32px;border-radius:50%;background:var(--orange)}
.subscribe ul{position:absolute;left:10px;top:50px}
.subscribe li{color:#fff;font-size:8.5px;line-height:14px;text-decoration:underline}
.sub-bar{position:absolute;left:0;bottom:0;width:170px;height:33px;background:#333;color:#fff;padding:9px 0 0 10px;font-size:8px}
.sub-bar b{font-size:13px;margin-right:3px}
.join{position:absolute;left:120px;top:8px;width:45px;height:16px;background:var(--orange);border-radius:2px;color:#fff;font-size:8px;text-align:center;line-height:16px}

/* footer */
.footer{left:0;top:1023px;width:811px;height:177px;background:var(--blue-footer)}
.footer-col{color:#fff}
.footer-col h4{font-weight:400;font-size:8.5px;margin-bottom:6px}
.footer-col li{font-size:8.5px;line-height:12.8px;padding-left:11px;position:relative}
.footer-col li::before{content:"";position:absolute;left:1px;top:4px;width:5px;height:5px;border-radius:50%;background:#fff}
.col-sitemap{left:96px;top:1050px}
.col-services{left:182px;top:1050px}
.map{left:295px;top:1051px;width:116px;height:96px;background:linear-gradient(135deg,#e6e2d8,#d4d9c9);border:2px solid #fff}
.col-contact{left:421px;top:1050px;width:140px;font-size:8px;line-height:11px}
.pill{position:absolute;left:421px;width:127px;height:16px;background:#fff;color:#333;font-size:7.5px;line-height:16px;padding-left:16px}
.pill::before{content:"";position:absolute;left:5px;top:5px;width:7px;height:6px;background:#444}
.pill.email{top:1101px}.pill.phone{top:1123px}
.foot-brand{left:588px;top:1079px;display:flex;align-items:center;gap:5px}
.foot-brand .dot{width:18px;height:18px;border-radius:50%;background:var(--footer-mark)}
.foot-brand span{font-family:"Questrial",sans-serif;font-size:15px;color:var(--footer-mark)}
.check-in{left:584px;top:1114px;width:127px;height:35px;border-radius:18px;background:linear-gradient(#53c34a,#23911f);border:2px solid #fff;color:#fff;font-family:"Questrial",sans-serif;font-size:19px;text-align:center;line-height:31px;box-shadow:0 2px 3px rgba(0,0,0,.3)}
.footer-rule{left:96px;top:1163px;width:620px;height:1px;background:rgba(255,255,255,.3)}
.copyright{left:96px;top:1180px;font-size:7.5px;color:#fff}
</style>
</head>
<body>

<header class="abs masthead">
  <div class="abs brand"><div class="brand-dot"></div><span class="brand-name">Larkmoor Medical</span></div>
  <div class="abs account register">&#9679; Register</div>
  <div class="abs account login">&#9679; Log In</div>
  <div class="abs account blog">&#9679; Blog</div>
  <ul class="abs primary-nav">
    <li>Home</li><li>About</li><li class="active">Services</li><li>Staff</li><li>Insurance</li><li>Videos</li><li>Contact Us</li>
  </ul>
</header>

<ul class="abs services-menu">
  <li>Immediate Care</li><li>Allergies</li><li>Primary Care</li><li>Women's Health</li><li>Medical Spa</li><li>Treatments</li><li>Men's Health</li><li>Weight Loss</li>
</ul>

<section class="abs hero" role="img" aria-label="Slider photo of a smiling family on grass with a city skyline under a blue sky"></section>
<h1 class="abs hero-title">Concierge-Quality healthcare.<br>For your whole Family</h1>
<form class="abs appointment">
  <h2>Request An Appointment</h2>
  <div class="field" style="left:10px;top:34px">Name</div>
  <div class="field" style="left:140px;top:34px">Email Address</div>
  <div class="field" style="left:10px;top:61px">Zip Code</div>
  <div class="field" style="left:140px;top:61px">Phone</div>
  <span class="required">All fields required</span>
  <span class="submit">Submit</span>
</form>
<div class="abs hint">Please Enter Email</div>
<svg class="abs slide-arrow prev" viewBox="0 0 26 26"><path d="M15 7l-6 6 6 6" stroke="#fff" stroke-width="2.5" fill="none"/></svg>
<svg class="abs slide-arrow next" viewBox="0 0 26 26"><path d="M11 7l6 6-6 6" stroke="#fff" stroke-width="2.5" fill="none"/></svg>

<h2 class="abs welcome">Welcome to the Larkmoor <span>Medical</span></h2>
<div class="abs welcome-rule"></div>
<div class="abs welcome-dot"></div>

<article class="abs feature" style="left:97px">
  <svg class="feature-icon" viewBox="0 0 30 30"><circle cx="15" cy="15" r="8" fill="none" stroke="#fff" stroke-width="2"/><path d="M15 10v5h4" stroke="#fff" stroke-width="2" fill="none"/></svg>
  <h3>It's about time</h3>
  <p>Lorem Ipsum is simply dummy text of the printing and typesetting industry. Lorem Ipsum has been the industry's standard dummy text ever since the 1500s, when an unknown printer took a galley of type and scrambled it.</p>
</article>
<article class="abs feature" style="left:315px">
  <svg class="feature-icon" viewBox="0 0 30 30"><path d="M15 6l2.6 5.6 6 .7-4.5 4.1 1.2 6-5.3-3-5.3 3 1.2-6-4.5-4.1 6-.7z" fill="#fff"/></svg>
  <h3>It's about choices</h3>
  <p>Lorem Ipsum is simply dummy text of the printing and typesetting industry. Lorem Ipsum has been the industry's standard dummy text ever since the 1500s, when an unknown printer took a galley of type and scrambled it.</p>
</article>
<article class="abs feature" style="left:534px">
  <svg class="feature-icon" viewBox="0 0 30 30"><circle cx="15" cy="11" r="4" fill="#fff"/><path d="M8 23c0-5 3-7 7-7s7 2 7 7z" fill="#fff"/></svg>
  <h3>It's about you</h3>
  <p>Lorem Ipsum is simply dummy text of the printing and typesetting industry. Lorem Ipsum has been the industry's standard dummy text ever since the 1500s, when an unknown printer took a galley of type and scrambled it.</p>
</article>

<section class="abs lab">
  <h2>Our In-House Lab Makes Testing Quick and Accurate</h2>
  <p class="lab-intro">Larkmoor Medical offers fast, accurate test results from our in-house lab. That way you know your test results sooner. Here are some of the common tests we perform on premises....</p>
  <div class="lab-photo" role="img" aria-label="Photo of a mother and child sitting in a sunny field"></div>
  <p class="lab-text">Lorem Ipsum is simply dummy text of the printing and typesetting industry. Lorem Ipsum has been the industry's standard dummy text ever since the 1500s, when an unknown printer took a galley of type and scrambled it.</p>
  <ul class="tests">
    <li>Electrocardiograph (EKG)</li><li>Pulmonary Function test</li><li>STD Testing</li><li>Comprehensive blood tests</li>
  </ul>
  <span class="read-more">Rea More</span>
  <blockquote class="quote">Lorem Ipsum is simply dummy text of the printing and typesetting industry. Lorem Ipsum has been the industry's standard dummy text ever since the 1500s, when an unknown printer took a galley of type and scrambled it..</blockquote>
  <div class="avatar" role="img" aria-label="Portrait photo of the reviewer"></div>
  <p class="person"><b>Owen Hale</b>From: London<br>Production Manager</p>
  <span class="view-all">view all</span>
</section>

<aside>
  <div class="abs no-appt">
    <svg class="abs" style="left:11px;top:9px" width="18" height="18" viewBox="0 0 18 18"><rect x="2" y="3" width="12" height="13" fill="none" stroke="#fff" stroke-width="1.5"/><path d="M7 11l9-9" stroke="#fff" stroke-width="2"/></svg>
    No Appointment?<br>No Problem
  </div>
  <div class="abs search"><div>Search...
    <svg class="abs" style="right:5px;top:3px" width="10" height="10" viewBox="0 0 10 10"><circle cx="4" cy="4" r="3" fill="none" stroke="#333" stroke-width="1.4"/><path d="M6.3 6.3L9.5 9.5" stroke="#333" stroke-width="1.6"/></svg>
  </div></div>
  <div class="abs video" role="img" aria-label="Video thumbnail of a family smiling together">
    <svg class="play" width="24" height="24" viewBox="0 0 24 24"><circle cx="12" cy="12" r="11" fill="#222" stroke="#fff" stroke-width="1.5"/><path d="M9.5 7.5l7 4.5-7 4.5z" fill="#fff"/></svg>
  </div>
  <div class="abs subscribe">
    <h2>Subscribe</h2>
    <div class="feed-dot"></div>
    <ul><li>RSS Feed</li><li>Email Subscription</li><li>Learn more</li></ul>
    <div class="sub-bar"><b>363</b> subscribers<span class="join">Join 'em?</span></div>
  </div>
</aside>

<footer class="abs footer"></footer>
<div class="abs footer-col col-sitemap">
  <h4>Site Map</h4>
  <ul><li>Home</li><li>About</li><li>Services</li><li>Staff</li><li>Insurance</li><li>Videos</li></ul>
</div>
<div class="abs footer-col col-services">
  <h4>Our Services</h4>
  <ul><li>Lorem Ipsum is</li><li>simply dummy</li><li>text of the printing</li><li>and typesetting</li><li>industry. Lorem</li><li>Ipsum has been</li></ul>
</div>
<div class="abs map" role="img" aria-label="Street map showing the clinic location"></div>
<div class="abs footer-col col-contact">
  <h4>Contact us</h4>
  LarkmoorFamilyMedical.example<br>4120 Larkmoor Ave ( at Elm Rd )<br>Ste 210, Elmford, TX 70012
</div>
<div class="pill email">E-mail : info@lkmedical.example</div>
<div class="pill phone">( 214) 555 0148</div>
<div class="abs foot-brand"><div class="dot"></div><span>Larkmoor Medical</span></div>
<div class="abs check-in">Check In</div>
<div class="abs footer-rule"></div>
<p class="abs copyright">© copyright 2012 LarkmoorFamilyMedical.example</p>

</body>
</html>
```